Newsletter Design for Travel - Group -Event Agency

We are looking for a standard Newsletter Design which we can use regularly to send out to a number of clients. The idea is to add 1 or more pictures and a promotion or program as well as some possible news. We are a travel agency and want to promote our products in either the travel sector (B2C) or event and group sector (B2B , see our company logo enclosed.

Target Market(s)

We have different target markets, but in the end it's always connected to the travel industry

Industry/Entity Type

Events

Font styles to use
Sans Serif

Colors
3176b5
eaf1f7

Requirements
Must have
• Area to upload picture(s), text field and business data (website, linkedin, facebook, instagram, tel and e-mail contacts. Subscribe/unsubscrive
Nice to have
• optional CTA Buttom, p.e. "make a virutal appointment" or similar
Should not have
• should stay with the colours of our logo / website - grey, a bit blue

```html
<!DOCTYPE html>
<html lang="en">
<head>
<meta charset="utf-8">
<title>Marea Journeys Newsletter</title>
<link rel="stylesheet" href="https://fonts.googleapis.com/css2?family=Montserrat:wght@400;500;600;700&display=swap">
<style>
  :root {
    --brand-blue: #1073b7;
    --brand-blue-light: #eaf1f7;
    --ink: #1a1a1a;
    --bar-grey: #5c626b;
    --footer-grey: #dcdde0;
    --button-grey: #7a7a7a;
    --page: #efefef;
    --white: #ffffff;
  }
  * { box-sizing: border-box; margin: 0; padding: 0; }
  html, body { width: 1200px; height: 1147px; overflow: hidden; }
  body {
    background: var(--page);
    font-family: "Montserrat", sans-serif;
    color: var(--ink);
    position: relative;
  }
  .newsletter {
    position: absolute;
    top: 98px;
    width: 476px;
    background: var(--white);
    display: flex;
    flex-direction: column;
  }
  .newsletter--classic { left: 99px; }
  .newsletter--grid { left: 631px; }

  .masthead {
    display: flex;
    flex-direction: column;
    align-items: center;
    justify-content: center;
  }
  .brand-name {
    font-weight: 700;
    font-size: 27px;
    letter-spacing: 1px;
    color: var(--ink);
    line-height: 1;
  }
  .brand-tagline {
    margin-top: 8px;
    font-weight: 600;
    font-size: 8.5px;
    letter-spacing: 3.4px;
    color: var(--brand-blue);
  }

  .photo { display: block; width: 100%; }

  .hero { position: relative; height: 275px; }
  .hero .photo { height: 100%; background: linear-gradient(180deg, #8ec3e8 0%, #b9dcef 25%, #d9bf86 50%, #39b7c4 75%, #2aa3b0 100%); }
  .hero-panel {
    position: absolute; left: 0; top: 68px;
    width: 277px; height: 144px;
    background: rgba(234, 241, 247, 0.72);
    padding: 30px 20px 0 24px;
  }
  .section-title { font-weight: 500; font-size: 20px; line-height: 1.1; }
  .body-copy { font-weight: 500; font-size: 7px; line-height: 13.7px; }
  .hero-panel .body-copy { margin-top: 12px; }

  .feature {
    height: 214px;
    background: var(--brand-blue);
    color: var(--white);
    text-align: center;
    padding: 48px 54px 0;
  }
  .feature .body-copy { margin-top: 12px; }
  .button {
    display: inline-block;
    font-weight: 600;
    font-size: 8px;
    letter-spacing: 0.3px;
    line-height: 1;
    text-decoration: none;
  }
  .button--light { margin-top: 16px; background: var(--white); color: var(--ink); padding: 5px 17px; }
  .button--grey { margin-top: 18px; background: var(--button-grey); color: var(--ink); padding: 4px 17px; }
  .button--blue { margin-top: 8px; background: var(--brand-blue); color: var(--white); padding: 4px 16px; font-size: 7px; }

  .forest { height: 210px; background: linear-gradient(180deg, #1e5a24 0%, #2f8a2e 40%, #1d6b3b 70%, #21b6a5 100%); }

  .contact {
    display: flex; flex-direction: column; align-items: center;
    text-align: center;
  }
  .contact--white { height: 111px; padding-top: 18px; }
  .contact--grey { height: 110px; padding-top: 18px; background: var(--footer-grey); color: #555; }
  .social { display: flex; gap: 11px; }
  .social-dot { width: 26px; height: 26px; border-radius: 50%; background: var(--brand-blue); }
  .contact--grey .social-dot { background: var(--bar-grey); }
  .contact .fine-print { margin-top: 10px; font-size: 6px; line-height: 13.7px; width: 300px; }

  .site-bar {
    height: 21px; background: var(--bar-grey); color: var(--white);
    font-size: 9px; letter-spacing: 5.5px; font-weight: 500;
    display: flex; align-items: center; justify-content: center;
  }

  .spotlight { position: relative; height: 372px; background: var(--brand-blue); }
  .spotlight .photo {
    position: absolute; left: 24px; top: 20px; width: 427px; height: 286px;
    background: linear-gradient(180deg, #2b56a8 0%, #4a74c0 45%, #8c7a5c 70%, #3c6b2f 100%);
  }
  .spotlight-card {
    position: absolute; left: 77px; top: 241px; width: 322px; height: 117px;
    background: var(--white); text-align: center; padding: 25px 24px 0;
  }

  .destinations { height: 329px; display: flex; padding: 21px 25px 0; gap: 15px; }
  .destination { width: 132px; display: flex; flex-direction: column; align-items: center; text-align: center; }
  .destination .photo { height: 140px; }
  .destination .section-title { margin-top: 20px; font-size: 19.5px; white-space: nowrap; }
  .destination .body-copy { margin-top: 10px; width: 134px; }
  .photo--dusk { background: linear-gradient(180deg, #3a1d10 0%, #8a4a1c 55%, #f0a53a 100%); }
  .photo--lanterns { background: linear-gradient(180deg, #2f3a1c 0%, #7b5a2a 50%, #c7643a 100%); }
  .photo--lagoon { background: linear-gradient(180deg, #7fb6e6 0%, #5a8a4a 45%, #2c8fd0 100%); }
</style>
</head>
<body>

<article class="newsletter newsletter--classic">
  <header class="masthead" style="height:90px">
    <div class="brand-name">MAREA JOURNEYS</div>
    <div class="brand-tagline">TRAVEL - GROUPS - EVENTS</div>
  </header>

  <section class="hero">
    <div class="photo" role="img" aria-label="Coastal cliffs above a turquoise sea"></div>
    <div class="hero-panel">
      <h2 class="section-title">Lorem ipsum</h2>
      <p class="body-copy">Lorem ipsum dolor sit amet, consectetuer adipiscing elit, sed diam nonummy nibh euismod tincidunt ut laoreet dolore magna aliquam erat volutpat. Ut wisi enim ad minim veniam, quis nostrud exerci tation.</p>
    </div>
  </section>

  <section class="feature">
    <h2 class="section-title">Lorem ipsum</h2>
    <p class="body-copy">Lorem ipsum dolor sit amet, consectetuer adipiscing elit, sed diam nonummy nibh euismod tincidunt ut laoreet dolore magna aliquam erat volutpat. Ut wisi enim ad minim veniam, quis nostrud exerci tation ullamcorper suscipit lobortis nisl ut aliquip ex ea commodo consequat. Duis autem vel eum iriure dolor in hendrerit .</p>
    <a class="button button--light" href="#">SEE MORE</a>
  </section>

  <div class="photo forest" role="img" aria-label="Waterfall falling into a green pool in a fern forest"></div>

  <footer class="contact contact--white">
    <div class="social" aria-label="Social links">
      <span class="social-dot"></span><span class="social-dot"></span><span class="social-dot"></span><span class="social-dot"></span>
    </div>
    <p class="fine-print">Lorem ipsum dolor sit amet, consectetuer adipiscing elit, sed diam nonummy nibh euismod tincidunt ut laoreet dolore magna aliquam erat volutpat. Ut wisi enim ad minim veniam, quis nostrud exerci tation.</p>
  </footer>
  <div class="site-bar">www.mareajourneys.com</div>
</article>

<article class="newsletter newsletter--grid">
  <header class="masthead" style="height:88px">
    <div class="brand-name">MAREA JOURNEYS</div>
    <div class="brand-tagline">TRAVEL - GROUPS - EVENTS</div>
  </header>

  <section class="spotlight">
    <div class="photo" role="img" aria-label="Traditional thatched A-frame house under a blue sky"></div>
    <div class="spotlight-card">
      <p class="body-copy">Lorem ipsum dolor sit amet, consectetuer adipiscing elit, sed diam nonummy nibh euismod tincidunt ut laoreet dolore magna aliquam erat volutpat. Ut wisi enim ad.</p>
      <a class="button button--grey" href="#">SEE MORE</a>
    </div>
  </section>

  <section class="destinations">
    <div class="destination">
      <div class="photo photo--dusk" role="img" aria-label="Carved rock temple lit by candles at night"></div>
      <h3 class="section-title">Lorem ipsum</h3>
      <p class="body-copy">Lorem ipsum dolor sit amet, consectetuer adipiscing elit, sed diam nonummy nibh euismod tincidunt ut laoreet dolore magna aliquam erat volutpat.</p>
      <a class="button button--blue" href="#">SEE MORE</a>
    </div>
    <div class="destination">
      <div class="photo photo--lanterns" role="img" aria-label="Paper lanterns released at an evening festival"></div>
      <h3 class="section-title">Lorem ipsum</h3>
      <p class="body-copy">Lorem ipsum dolor sit amet, consectetuer adipiscing elit, sed diam nonummy nibh euismod tincidunt ut laoreet dolore magna aliquam erat volutpat.</p>
      <a class="button button--blue" href="#">SEE MORE</a>
    </div>
    <div class="destination">
      <div class="photo photo--lagoon" role="img" aria-label="Limestone islands rising from a calm bay"></div>
      <h3 class="section-title">Lorem ipsum</h3>
      <p class="body-copy">Lorem ipsum dolor sit amet, consectetuer adipiscing elit, sed diam nonummy nibh euismod tincidunt ut laoreet dolore magna aliquam erat volutpat.</p>
      <a class="button button--blue" href="#">SEE MORE</a>
    </div>
  </section>

  <footer class="contact contact--grey">
    <div class="social" aria-label="Social links">
      <span class="social-dot"></span><span class="social-dot"></span><span class="social-dot"></span><span class="social-dot"></span>
    </div>
    <p class="fine-print">Lorem ipsum dolor sit amet, consectetuer adipiscing elit, sed diam nonummy nibh euismod tincidunt ut laoreet dolore magna aliquam erat volutpat. Ut wisi enim ad minim veniam, quis nostrud exerci tation.</p>
  </footer>
  <div class="site-bar">www.mareajourneys.com</div>
</article>

</body>
</html>
```